Business Card, Stationary with Shark Logo for Personal Injury Lawyer

I need business cards and stationery with a shark logo for my Personal Injury Law Practice. Has to have this written on it:
Martin K. Hollis
Injury Lawyer
The Corvell Building
718 Tandy Street
Providence, Rhode Island 02908
401-627-4193
Martinhollis.com

Contact Information for Business Card

Martin K. Hollis, Injury Lawyer, address, 401-627-4193, martinhollis.com

```html
<!DOCTYPE html>
<html lang="en">
<head>
<meta charset="utf-8">
<title>Martin K. Hollis – Business Card</title>
<link href="https://fonts.googleapis.com/css2?family=Arimo:wght@400;700&display=swap" rel="stylesheet">
<style>
  :root {
    --navy: #29245f;
    --ink: #4a4a4a;
    --rule: #555555;
    --swoosh: #b4b4b4;
    --paper: #ffffff;
    --backdrop: #ececee;
  }
  * { margin: 0; padding: 0; box-sizing: border-box; }
  html, body {
    width: 1200px; height: 1200px; overflow: hidden;
    background: var(--backdrop);
    font-family: "Arimo", Arial, sans-serif;
  }
  .card {
    position: absolute;
    left: 298px;
    width: 605px;
    height: 346px;
    overflow: hidden;
  }
  .card-front { top: 218px; background: var(--paper); }
  .card-back { top: 636px; background: var(--navy); }

  .wave { position: absolute; left: 0; top: 0; width: 605px; height: 346px; }

  .wordmark {
    position: absolute;
    font-weight: 700;
    white-space: nowrap;
    letter-spacing: 0.2px;
  }
  .card-front .wordmark {
    left: 66px; top: 146px;
    font-size: 26px;
    color: var(--navy);
  }
  .card-back .wordmark {
    left: 0; right: 0; top: 154px;
    text-align: center;
    font-size: 38px;
    color: var(--paper);
  }

  .rule { position: absolute; left: 311px; }
  .rule-accent { top: 82px; height: 37px; width: 4px; background: var(--navy); }
  .rule-thin { top: 147px; height: 97px; width: 2px; background: var(--rule); left: 312px; }

  .details { position: absolute; left: 350px; top: 80px; color: var(--ink); font-size: 14px; line-height: 17.5px; }
  .name { font-size: 24px; font-weight: 700; color: var(--navy); line-height: 26px; }
  .title { margin-top: 0; }
  .address { margin-top: 19px; }
  .contact { margin-top: 19px; list-style: none; }
  .contact li { display: flex; align-items: center; gap: 6px; }
  .contact svg { width: 12px; height: 12px; fill: var(--navy); flex: none; }
</style>
</head>
<body>
  <section class="card card-front">
    <svg class="wave" viewBox="0 0 605 346" aria-hidden="true">
      <path d="M0,246 C180,292 420,334 575,293 C420,326 190,304 0,256 Z" fill="var(--swoosh)"/>
      <path d="M0,262 C200,310 470,340 605,275 L605,346 L0,346 Z" fill="var(--navy)"/>
    </svg>

    <div class="wordmark">Martin K. Hollis</div>

    <div class="rule rule-accent"></div>
    <div class="rule rule-thin"></div>

    <div class="details">
      <div class="name">Martin K. Hollis</div>
      <div class="title">Injury Lawyer</div>
      <div class="address">718 Tandy St<br>Providence, RI 02908</div>
      <ul class="contact">
        <li>
          <svg viewBox="0 0 24 24"><path d="M6.6 10.8a15 15 0 0 0 6.6 6.6l2.2-2.2a1 1 0 0 1 1-.25 11.4 11.4 0 0 0 3.6.57 1 1 0 0 1 1 1V20a1 1 0 0 1-1 1A17 17 0 0 1 3 4a1 1 0 0 1 1-1h3.5a1 1 0 0 1 1 1c0 1.25.2 2.45.57 3.57a1 1 0 0 1-.25 1z"/></svg>
          (401) 627-4193
        </li>
        <li>
          <svg viewBox="0 0 24 24"><path d="M2 5h20v14H2z M4 7v.5l8 5.5 8-5.5V7z" fill-rule="evenodd"/></svg>
          martin@martinhollis.com
        </li>
        <li>
          <svg viewBox="0 0 24 24"><path d="M12 2a10 10 0 1 0 0 20 10 10 0 0 0 0-20zm6.9 9h-3a15 15 0 0 0-1.4-6.3A8 8 0 0 1 18.9 11zM12 4.1c1 1.4 1.8 3.9 1.9 6.9h-3.8c.1-3 .9-5.5 1.9-6.9zM9.5 4.7A15 15 0 0 0 8.1 11h-3a8 8 0 0 1 4.4-6.3zM5.1 13h3a15 15 0 0 0 1.4 6.3A8 8 0 0 1 5.1 13zm6.9 6.9c-1-1.4-1.8-3.9-1.9-6.9h3.8c-.1 3-.9 5.5-1.9 6.9zm2.5-.6a15 15 0 0 0 1.4-6.3h3a8 8 0 0 1-4.4 6.3z"/></svg>
          martinhollis.com
        </li>
      </ul>
    </div>
  </section>

  <section class="card card-back">
    <div class="wordmark">Martin K. Hollis</div>
  </section>
</body>
</html>
```